Design and code BigCommerce website

Website is currently up and running but looking for a fresh and new theme or design for it.

Must interact perfectly with BigCommerce

Will provide plenty of images.

All content should stay exactly the same as far as text and information.

Looking for a dark but elegant theme. All of the information necessary is listed.

Will need detailed instructions on how to implement the website into our current system... simply looking to make our page unique and not just a stock BigCommerce theme

Coding

Coded - Design and coding required

Number of Pages Required

5+ page

Colors
000000
9d9d9d
ffffff

Requirements
Must have
• same information as www.pellowbrookdrops.com

```html
<!DOCTYPE html>
<html lang="en">
<head>
<meta charset="utf-8">
<title>Pellowbrook Drops — Welcome</title>
<link rel="stylesheet" href="https://fonts.googleapis.com/css2?family=Oswald:wght@500&family=Poiret+One&display=swap">
<style>
  :root {
    --bg: #1b1b1b;
    --gold: #f5b80a;
    --text-light: #e6e6e6;
    --text-muted: #cfcfcf;
    --logo-ink: #2b2b2b;
    --glow: #a9a9a9;
  }
  * { margin: 0; padding: 0; box-sizing: border-box; }
  html, body { width: 1200px; height: 936px; overflow: hidden; background: var(--bg); }
  .page { position: relative; width: 1200px; height: 936px; background: var(--bg); overflow: hidden; }

  .spotlight { position: absolute; left: 0; top: 0; width: 1200px; height: 936px; }

  .brand-glow {
    position: absolute; left: 410px; top: 28px; width: 380px; height: 170px;
    background: radial-gradient(ellipse at 50% 48%, var(--glow) 0%, #8a8a8a 38%, rgba(80,80,80,0.5) 62%, rgba(27,27,27,0) 78%);
  }
  .brand-name {
    position: absolute; left: 0; top: 86px; width: 1200px; text-align: center;
    font-family: "Poiret One", sans-serif; font-size: 36px; color: var(--logo-ink);
    letter-spacing: 1px;
  }

  .intro-ring {
    position: absolute; left: 300px; top: 241px; width: 600px; height: 600px;
    border: 1.2px solid var(--gold); border-radius: 50%;
  }
  .intro {
    position: absolute; left: 340px; top: 388px; width: 520px; text-align: center;
  }
  .intro-kicker {
    font-family: "Poiret One", sans-serif; font-size: 50px; line-height: 50px;
    color: var(--text-muted); letter-spacing: -1px;
  }
  .intro-title {
    margin-top: 2px;
    font-family: "Oswald", sans-serif; font-weight: 500; font-size: 52px; line-height: 56px;
    color: var(--gold);
  }
  .intro-text {
    margin: 24px auto 0; width: 496px;
    font-family: "Poiret One", sans-serif; font-size: 16.5px; line-height: 21.6px;
    color: var(--text-light);
  }
  .intro-arrow { position: absolute; left: 554px; top: 664px; width: 88px; height: 20px; }
</style>
</head>
<body>
<main class="page">
  <svg class="spotlight" viewBox="0 0 1200 936" aria-hidden="true">
    <defs>
      <linearGradient id="beam" x1="0" y1="0" x2="0" y2="1">
        <stop offset="0" stop-color="#3a3a3a" stop-opacity="0"/>
        <stop offset="0.55" stop-color="#363636" stop-opacity="0.9"/>
        <stop offset="1" stop-color="#2a2a2a" stop-opacity="0.6"/>
      </linearGradient>
      <filter id="soft" x="-20%" y="-20%" width="140%" height="140%">
        <feGaussianBlur stdDeviation="14"/>
      </filter>
    </defs>
    <polygon points="60,640 1140,640 1120,680 600,845 80,680" fill="url(#beam)" filter="url(#soft)"/>
  </svg>

  <header class="brand">
    <div class="brand-glow"></div>
    <p class="brand-name">Pellowbrook Drops</p>
  </header>

  <div class="intro-ring"></div>
  <section class="intro">
    <h2 class="intro-kicker">WELCOME TO</h2>
    <h1 class="intro-title">PELLOWBROOK DROPS</h1>
    <p class="intro-text">Lorem Ipsum is simply dummy text of the printing and typesetting industry. Lorem Ipsum has been the industry's standard dummy text ever since the 1500s, when an unknown printer took a galley of type and scrambled it to make a type specimen book. It has survived not only five centuries.</p>
  </section>

  <svg class="intro-arrow" viewBox="0 0 88 20" aria-label="Continue">
    <line x1="0" y1="10" x2="76" y2="10" stroke="var(--gold)" stroke-width="2.5"/>
    <path d="M60 2 L86 10 L60 18 L68 10 Z" fill="var(--gold)"/>
  </svg>
</main>
</body>
</html>
```